依頼詳細
頂いている参考サイトとしては下記のURLがありますが、
先方でもどのデザインの何が良いのかは計りかねているらしく、
下記を参考に様々な形式でデザインを作成して欲しいということです。

‣SUNPEBBLE https://www.sunpebble42.jp/biwako-sup/ ➡デザインが素敵
‣富岡興 https://www.tomiokako.co.jp/ja/ ➡ 大企業感
‣学びの扉本部 https://www.manabitobira.jp/  ➡ 同コンセプト

また、事業内容は現在のページに準拠するということで、現在サイトのパスはmizetとなります。

TOPページへの掲載内容については、
TOPイメージ
事業内容
採用情報
新着情報
となります。
サイトURL
http://feln.co.jp/
ページ数
1ページ
希望イメージ
シンプル 複雑
単色 カラフル
暗い 明るい
日常 高級
遊び心 厳粛
未来的 伝統的
女性的 男性的
希望する色
緑系
納品ファイル
• フォトショップ形式 (.psd)
補足説明
依頼公開後の追記内容
現行サイトのパスワードについて失念しておりました。
パスワードは mizet となります。

デザインが特に先方に気に入られたため

この度はご提案をいただきまして、誠にありがとうございました。
また機会がありましたら、よろしくお願い致します。

```html
<!DOCTYPE html>
<html lang="ja">
<head>
<meta charset="UTF-8">
<title>株式会社フェルン</title>
<link href="https://fonts.googleapis.com/css2?family=Noto+Sans+JP:wght@400;500;700&family=Noto+Serif+JP:wght@500;700&display=swap" rel="stylesheet">
<style>
:root{
  --green:#0b8f3f;
  --green-dark:#06702f;
  --green-light:#3fb35f;
  --ink:#333;
  --muted:#888;
  --line:#ddd;
  --paper:#fff;
  --soft:#f4f5f4;
  --blue:#2a62b8;
}
*{margin:0;padding:0;box-sizing:border-box}
html,body{width:1200px;height:2184px;overflow:hidden}
body{font-family:"Noto Sans JP",sans-serif;color:var(--ink);background:var(--paper);position:relative}
.serif{font-family:"Noto Serif JP",serif}

.site-header{position:absolute;top:0;left:0;width:1200px;height:44px;background:var(--paper);display:flex;align-items:center;padding:0 0 0 22px;z-index:3}
.brand{display:flex;align-items:center;gap:8px;font-size:13px;font-weight:700;color:var(--green)}
.brand-dot{width:18px;height:18px;border-radius:50%;background:var(--green)}
.global-nav{margin-left:auto;display:flex;height:44px}
.global-nav a{display:flex;align-items:center;padding:0 18px;font-size:11px;color:var(--ink);text-decoration:none;border-left:1px solid var(--line)}
.global-nav a.current{color:var(--green)}
.global-nav a.nav-contact{background:var(--green);color:#fff;padding:0 26px;border:none}

.hero{position:absolute;top:44px;left:0;width:1200px;height:520px;background:linear-gradient(110deg,#b9aea3 0%,#d8d2cb 35%,#ece9e4 60%,#cfd3d1 100%)}
.hero-copy{position:absolute;left:130px;top:110px;color:#fff;font-size:30px;line-height:1.7;letter-spacing:.08em;text-shadow:0 1px 6px rgba(0,0,0,.25)}
.hero-badge{position:absolute;right:36px;top:342px;width:120px;height:34px;background:#fff;border-radius:3px}

.news-head{position:absolute;left:0;top:400px;width:300px;height:190px;background:var(--green);color:#fff;padding:32px 0 0 36px}
.news-head h2{font-size:24px;letter-spacing:.1em;font-weight:500}
.news-head small{display:block;font-size:10px;margin-top:2px}
.news-head .more{display:inline-block;margin-top:30px;border:1px solid #fff;padding:4px 22px;font-size:10px}
.news-list{position:absolute;left:330px;top:452px;width:800px;list-style:none}
.news-list li{display:flex;align-items:center;height:40px;border-bottom:1px solid var(--line);font-size:10px}
.news-list time{width:110px;color:var(--muted)}
.tag{width:90px;text-align:center;color:#fff;font-size:9px;padding:2px 0;margin-right:28px}
.tag.g{background:var(--green)}.tag.b{background:var(--blue)}
.news-list .more-link{position:absolute;right:-50px;top:-44px;font-size:10px;color:var(--green)}

.section-title{position:absolute;left:0;width:1200px;text-align:center}
.section-title h2{font-size:22px;letter-spacing:.14em;font-weight:500}
.section-title small{display:block;font-size:9px;color:var(--muted);margin-top:2px}

.biz{position:absolute;left:0;width:1200px;height:260px}
.biz-text{position:absolute;top:50px;width:300px}
.biz-text h3{font-size:17px;font-weight:700}
.biz-text small{display:block;font-size:9px;color:var(--muted);margin:2px 0 16px}
.biz-text p{font-size:10px;line-height:1.9;color:#555}
.btn{display:inline-block;margin-top:18px;border:1px solid var(--green);color:var(--green);font-size:10px;padding:5px 28px}
.biz-photo{position:absolute;top:0;height:260px}

.recruit-band{position:absolute;top:1300px;left:0;width:1200px;height:300px;background:linear-gradient(180deg,var(--green) 0%,var(--green-dark) 100%);color:#fff}
.recruit-band .section-title small{color:#cfe9d6}
.recruit-lead{position:absolute;left:240px;top:115px;border:1px solid #fff;padding:12px 24px;font-size:14px;font-weight:700}
.recruit-text{position:absolute;left:580px;top:105px;width:400px;font-size:10px;line-height:1.9}
.recruit-text .btn{border-color:#fff;color:#fff}
.staff-photo{position:absolute;left:260px;top:1500px;width:700px;height:300px;background:linear-gradient(180deg,#cfd8de 0%,#a9b3bb 100%)}

.contact{position:absolute;top:1830px;left:0;width:1200px;height:90px;border-bottom:1px solid var(--line);display:flex;align-items:center;padding:0 80px}
.contact h2{font-size:22px;letter-spacing:.14em;font-weight:500;width:240px}
.contact h2 small{display:block;font-size:9px;color:var(--muted);letter-spacing:0}
.contact p{font-size:10px;color:#555;width:440px}
.contact .btn{margin:0 0 0 auto;padding:8px 40px}

.site-footer{position:absolute;top:1940px;left:0;width:1200px;height:220px;padding:20px 80px}
.site-footer .brand{font-size:14px}
.address{margin-top:14px;font-size:9px;line-height:1.8;color:#555}
.footer-nav{position:absolute;left:580px;top:20px;display:grid;grid-template-columns:repeat(4,130px);row-gap:14px;font-size:10px;list-style:none}
.footer-nav li::before{content:"›";color:var(--green);margin-right:6px}
.copyright{position:absolute;bottom:0;left:0;width:1200px;height:24px;background:var(--green);color:#fff;font-size:9px;text-align:center;line-height:24px}
</style>
</head>
<body>

<header class="site-header">
  <div class="brand"><span class="brand-dot"></span>株式会社フェルン</div>
  <nav class="global-nav">
    <a class="current" href="#">トップページ</a>
    <a href="#">企業情報</a>
    <a href="#">事業内容</a>
    <a href="#">採用情報</a>
    <a class="nav-contact" href="#">お問い合わせ</a>
  </nav>
</header>

<section class="hero" role="img" aria-label="机に向かって勉強する女の子とランドセルの写真">
  <p class="hero-copy serif">学びの扉という一生の財産を<br>すべての子どもたちへ</p>
  <div class="hero-badge"></div>
</section>

<section class="news">
  <div class="news-head">
    <h2 class="serif">NEWS</h2><small>新着情報</small>
    <span class="more">一覧を見る</span>
  </div>
  <ul class="news-list">
    <li><time>2024.06.10</time><span class="tag g">お知らせ</span>夏期講習の受付を開始しました。詳しくは各教室までお問い合わせください。</li>
    <li><time>2024.05.28</time><span class="tag b">採用情報</span>新卒採用の会社説明会の日程を公開しました。ぜひご参加ください。</li>
    <li><time>2024.05.15</time><span class="tag g">お知らせ</span>新しい教室を開校いたしました。地域の皆さまのご来校をお待ちしております。</li>
    <li><time>2024.04.30</time><span class="tag g">お知らせ</span>ゴールデンウィーク期間中の営業日についてのご案内を掲載しました。</li>
  </ul>
</section>

<div class="section-title" style="top:700px"><h2 class="serif">INFORMATION</h2><small>事業内容</small></div>

<section class="biz" style="top:760px">
  <div class="biz-text" style="left:120px">
    <h3>教育事業部</h3><small>Education Division</small>
    <p>子どもたち一人ひとりの可能性を引き出す個別指導教室を運営しています。学ぶ楽しさを伝え、自ら考える力を育みます。</p>
    <span class="btn">詳しく見る</span>
  </div>
  <div class="biz-photo" role="img" aria-label="英単語カードとノートで学習する手元の写真" style="left:600px;width:600px;background:linear-gradient(135deg,#e9e4dc,#cfc7bb)"></div>
</section>

<section class="biz" style="top:1020px">
  <div class="biz-photo" role="img" aria-label="タイの寺院の写真" style="left:0;width:600px;background:linear-gradient(180deg,#9fb6c8 0%,#b9a982 60%,#7d6a48 100%)"></div>
  <div class="biz-text" style="left:700px">
    <h3>海外事業部</h3><small>Overseas Division</small>
    <p>アジアを中心に教育サービスを展開しています。現地の子どもたちへ質の高い学びを届け、国際的な人材育成に貢献します。</p>
    <span class="btn">詳しく見る</span>
  </div>
</section>

<section class="recruit-band">
  <div class="section-title" style="top:40px"><h2 class="serif">RECRUIT</h2><small>採用情報</small></div>
  <div class="recruit-lead">求めるFELN人材</div>
  <div class="recruit-text">
    <p>私たちは教育を通じて社会に貢献したいという想いを持つ仲間を募集しています。経験は問いません。熱意ある方のご応募をお待ちしています。</p>
    <span class="btn">詳しく見る</span>
  </div>
</section>
<div class="staff-photo" role="img" aria-label="スーツ姿の社員が並ぶ集合写真"></div>

<section class="contact">
  <h2 class="serif">CONTACT<small>お問い合わせ</small></h2>
  <p>お問い合わせは、メールフォームより承っております。</p>
  <span class="btn">メールフォームはこちら</span>
</section>

<footer class="site-footer">
  <div class="brand"><span class="brand-dot"></span>株式会社フェルン</div>
  <p class="address">〒650-0000<br>架空県青葉市緑町1-2-3 グリーンビル5F<br>TEL 000-000-0000 / FAX 000-000-0001</p>
  <ul class="footer-nav">
    <li>トップページ</li><li>企業情報</li><li>事業内容</li><li>採用情報</li>
    <li>教育事業部</li><li>海外事業部</li><li>新着情報</li><li>お問い合わせ</li>
  </ul>
  <div class="copyright">© FELN Co., Ltd. All Rights Reserved.</div>
</footer>

</body>
</html>
```